Velvetmoth chocolates label & packaging design

We make high end chocolates .Enrobed medjoul dates ,truffles and filled chocolates . We have to upgrade our packaging to reflect the quality of the products
1 . Chocolate box label or sleeve for
1a truffle box
2a enrobed date box
3a Chocolate box
4a Mixed chocolate truffle and date box .
I also have a project in mind to make hot chocolate kits which would be our hot chocolate powder chocolate & home made marshmallows.
The images attached should give an idea of the products The label designs included are an example of the colour palette we like .
We would like to include the velvetmoth logo as part of the design .
Our chocolates are made without adding. Dairy or refined sugars and using the best ingredients available .

Target Market(s)

Food lovers, those who prioritise quality above quantity .

Industry/Entity Type

Chocolatier

Font styles to use
Script

Colors
0054AA
0677BA
7BADD7
CADEEF
E8F1F8
F0912C
F2A743
F7CA91
FBE8D2
FDF5EE
E54698
E96AAD
F1A4CE
F9D9EA
FCEFF6

Requirements
Must have
• An element of luxury
Nice to have
• Something to reflect the integrity of the ingredients and the love that goes into making the chocolates.
Should not have
• Too much packaging

```html
<!DOCTYPE html>
<html lang="en">
<head>
<meta charset="utf-8">
<title>Velvetmoth Chocolates – Box Labels</title>
<link rel="stylesheet" href="https://fonts.googleapis.com/css2?family=Poiret+One&family=Sacramento&display=swap">
<style>
  :root {
    --backdrop: #9e9a98;
    --kraft: #cdb595;
    --kraft-edge: #bba283;
    --ink: #34343f;
    --paper: #f6f2ea;
    --teal: #6cc0c6;
    --navy: #2b3448;
    --rose: #cf6784;
  }
  * { box-sizing: border-box; margin: 0; padding: 0; }
  html, body { width: 1200px; height: 819px; overflow: hidden; }
  body {
    background: var(--backdrop);
    font-family: "Poiret One", sans-serif;
    color: var(--ink);
  }
  .label-row {
    position: absolute;
    left: 80px; top: 190px;
    display: flex; gap: 70px;
  }
  .box-label {
    position: relative;
    width: 300px; height: 440px;
    background: var(--kraft);
    border: 1px solid var(--kraft-edge);
    overflow: hidden;
  }
  .band {
    position: absolute; top: 0; bottom: 0;
    width: 22px;
    background: var(--accent);
  }
  .band--left { left: 14px; }
  .band--right { right: 14px; }
  .corner {
    position: absolute; width: 36px; height: 16px;
    background: var(--accent);
  }
  .corner--tl { top: 0; left: 0; }
  .corner--br { bottom: 0; right: 0; }
  .label--truffle-date { --accent: var(--teal); }
  .label--truffle { --accent: var(--navy); }
  .label--truffle .band { width: 16px; }
  .label--chocolate { --accent: var(--rose); }
  .label--chocolate .band--left { left: 0; width: 26px; }
  .label--chocolate .band--right { right: 0; width: 26px; }

  .title {
    position: absolute; top: 40px; left: 40px; right: 40px;
    text-align: center;
    font-size: 32px; letter-spacing: 2px;
    line-height: 1.05;
  }
  .title small { display: block; font-size: 24px; letter-spacing: 1px; }
  .brand-frame {
    position: absolute; left: 60px; top: 140px;
    width: 180px; height: 150px;
    background: var(--paper);
    border: 2px solid var(--ink);
    outline: 1px solid var(--ink);
    outline-offset: -7px;
    display: flex; flex-direction: column;
    align-items: center; justify-content: center;
    text-align: center;
  }
  .brand-name { font-size: 30px; line-height: 1; }
  .brand-sub { font-size: 15px; letter-spacing: 3px; margin-top: 10px; }
  .tagline {
    position: absolute; top: 318px; left: 40px; right: 40px;
    text-align: center;
    font-family: "Sacramento", cursive;
    font-size: 20px;
    white-space: nowrap;
  }
  .claim {
    position: absolute; top: 380px; left: 40px; right: 40px;
    text-align: center;
    font-family: "Sacramento", cursive;
    font-size: 13px;
    white-space: nowrap;
  }
  .zigzag {
    position: absolute; left: 40px; right: 40px; bottom: 16px;
    width: 220px; height: 10px;
  }
</style>
</head>
<body>
  <main class="label-row">
    <section class="box-label label--truffle-date">
      <div class="band band--left"></div>
      <div class="band band--right"></div>
      <div class="corner corner--tl"></div>
      <div class="corner corner--br"></div>
      <h2 class="title">TRUFFLE<small>AND DATE</small></h2>
      <div class="brand-frame">
        <span class="brand-name">velvetmoth</span>
        <span class="brand-name brand-sub">CHOCOLATES</span>
      </div>
      <p class="tagline">The best ingredients available</p>
      <p class="claim">Our Chocolates Are Made Without Adding</p>
      <svg class="zigzag" viewBox="0 0 220 10" preserveAspectRatio="none"><polyline fill="none" stroke="#34343f" stroke-width="1" points="0,0 5,10 10,0 15,10 20,0 25,10 30,0 35,10 40,0 45,10 50,0 55,10 60,0 65,10 70,0 75,10 80,0 85,10 90,0 95,10 100,0 105,10 110,0 115,10 120,0 125,10 130,0 135,10 140,0 145,10 150,0 155,10 160,0 165,10 170,0 175,10 180,0 185,10 190,0 195,10 200,0 205,10 210,0 215,10 220,0"/></svg>
    </section>

    <section class="box-label label--truffle">
      <div class="band band--left"></div>
      <div class="band band--right"></div>
      <div class="corner corner--tl"></div>
      <div class="corner corner--br"></div>
      <h2 class="title">TRUFFLE</h2>
      <div class="brand-frame">
        <span class="brand-name">velvetmoth</span>
        <span class="brand-name brand-sub">CHOCOLATES</span>
      </div>
      <p class="tagline">The best ingredients available</p>
      <p class="claim">Our Chocolates Are Made Without Adding</p>
      <svg class="zigzag" viewBox="0 0 220 10" preserveAspectRatio="none"><polyline fill="none" stroke="#34343f" stroke-width="1" points="0,0 5,10 10,0 15,10 20,0 25,10 30,0 35,10 40,0 45,10 50,0 55,10 60,0 65,10 70,0 75,10 80,0 85,10 90,0 95,10 100,0 105,10 110,0 115,10 120,0 125,10 130,0 135,10 140,0 145,10 150,0 155,10 160,0 165,10 170,0 175,10 180,0 185,10 190,0 195,10 200,0 205,10 210,0 215,10 220,0"/></svg>
    </section>

    <section class="box-label label--chocolate">
      <div class="band band--left"></div>
      <div class="band band--right"></div>
      <h2 class="title">CHOCOLATE</h2>
      <div class="brand-frame">
        <span class="brand-name">velvetmoth</span>
        <span class="brand-name brand-sub">CHOCOLATES</span>
      </div>
      <p class="tagline">The best ingredients available</p>
      <p class="claim">Our Chocolates Are Made Without Adding</p>
      <svg class="zigzag" viewBox="0 0 220 10" preserveAspectRatio="none"><polyline fill="none" stroke="#cf6784" stroke-width="1.5" points="0,0 5,10 10,0 15,10 20,0 25,10 30,0 35,10 40,0 45,10 50,0 55,10 60,0 65,10 70,0 75,10 80,0 85,10 90,0 95,10 100,0 105,10 110,0 115,10 120,0 125,10 130,0 135,10 140,0 145,10 150,0 155,10 160,0 165,10 170,0 175,10 180,0 185,10 190,0 195,10 200,0 205,10 210,0 215,10 220,0"/></svg>
    </section>
  </main>
</body>
</html>
```